Single Side Postcard Size Flyer Design

We want to design an attractive and eye-catching sign for hair stylists and barbers to sit on their workstations to attract the attention of their clients regarding hair loss and encourage them to speak to their stylist about it of they are would like to seek treatment.
Many men and women suffer from hair loss, but are often in denial it is happening or too embarrassed to talk about it.
This postcard sized flyer is designed to stick to the mirror at their hair stylist or barber and encourage them to ask their stylist about it.
We want this to be very plain and simple. With just perhaps some kind of simple head line and worry lines. I have uploaded a simple idea.
I have also uploaded the print templates that must be used to provide final designs.

Target Market(s)

Men aged 25 to 60 with thinning hair

Industry/Entity Type

Healthcare

Font styles to use
Sans Serif

Colors
0355a3
ffffff
cfcfcf
1b1b1b

Requirements
Must have
• Flyer size is vertical 4" x 6"
• Copy for the flyer is as follows ans is in color blue: #014ca5
• Worried About Thinning Hair?
• 2 out of 3 Men will have visible hair loss by age 35.
• The Good News is that your
• Barber or Stylist can tell you how to
• stop the loss & grow back your hair.
• Just ask.
• The Brisk Lattice Program from
• The Marlow Pine Company
• New Science. No Surgery. Your Hair.
• www.quellvantinfo.example
Should not have
• - dont add any logos, images or ornate design. this needs to be simple, easy to ready and eye catching.
• - do not use the color red in any capacity.

```html
<!DOCTYPE html>
<html lang="en">
<head>
<meta charset="utf-8">
<title>Worried About Thinning Hair? – Mirror Card</title>
<link rel="stylesheet" href="https://fonts.googleapis.com/css2?family=Open+Sans:wght@400;600;700;800&display=swap">
<style>
  :root {
    --brand-blue: #0355a3;
    --copy-blue: #014ca5;
    --white: #ffffff;
    --light-grey: #cfcfcf;
    --ink: #1b1b1b;
  }
  * { box-sizing: border-box; margin: 0; padding: 0; }
  html, body {
    width: 800px;
    height: 1200px;
    overflow: hidden;
    background: var(--white);
  }
  .card {
    width: 800px;
    height: 1200px;
    border: 12px solid var(--brand-blue);
    background: var(--white);
    display: flex;
    flex-direction: column;
    font-family: "Open Sans", Arial, sans-serif;
    color: var(--copy-blue);
  }
  .site-url {
    height: 94px;
    display: flex;
    align-items: center;
    justify-content: center;
    font-size: 26px;
    font-weight: 400;
    color: var(--ink);
  }
  .rule-dark { height: 18px; background: var(--ink); }
  .rule-grey { height: 16px; background: var(--light-grey); }
  .headline-panel {
    height: 262px;
    background: var(--brand-blue);
    color: var(--white);
    display: flex;
    flex-direction: column;
    justify-content: center;
    align-items: center;
    line-height: 1.12;
    text-align: center;
  }
  .headline-panel h1 {
    font-size: 76px;
    font-weight: 800;
    letter-spacing: -1px;
  }
  .headline-panel h1 .light { font-weight: 600; }
  .message {
    flex: 1;
    display: flex;
    flex-direction: column;
    align-items: center;
    text-align: center;
    padding-top: 48px;
  }
  .stat-lead {
    font-size: 36px;
    font-weight: 700;
    line-height: 1.15;
  }
  .stat-body {
    font-size: 27px;
    line-height: 1.4;
    color: var(--copy-blue);
    max-width: 600px;
  }
  .call-to-action {
    font-size: 112px;
    font-weight: 800;
    letter-spacing: -2px;
    line-height: 1;
    margin-top: 48px;
  }
  .program-credit {
    font-size: 27px;
    line-height: 1.4;
    margin-top: 28px;
  }
  .promise-strip {
    height: 72px;
    display: flex;
    font-size: 32px;
    font-weight: 600;
  }
  .promise-strip span {
    flex: 1;
    display: flex;
    align-items: center;
    justify-content: center;
  }
  .promise-science { background: var(--brand-blue); color: var(--white); }
  .promise-surgery { background: var(--light-grey); color: var(--ink); }
  .promise-hair { background: var(--ink); color: var(--white); }
</style>
</head>
<body>
  <main class="card">
    <div class="site-url">www.quellvantinfo.example</div>
    <div class="rule-dark"></div>
    <div class="rule-grey"></div>
    <section class="headline-panel">
      <h1>Worried About<br><span class="light">Thinning</span> Hair?</h1>
    </section>
    <div class="rule-grey"></div>
    <div class="rule-dark"></div>
    <section class="message">
      <p class="stat-lead">2 out of 3 Men</p>
      <p class="stat-body">will have visible hair loss by age 35.<br>
        The Good News is that your Barber<br>
        or Stylist can tell you how to stop<br>
        the loss &amp; grow back your hair.</p>
      <p class="call-to-action">Just ask.</p>
      <p class="program-credit">The Brisk Lattice Program<br>from The Marlow Pine Company</p>
    </section>
    <footer class="promise-strip">
      <span class="promise-science">New Science.</span>
      <span class="promise-surgery">No Surgery.</span>
      <span class="promise-hair">Your Hair.</span>
    </footer>
  </main>
</body>
</html>
```